SEO AND WEB DESIGN COMPANY BUSINESS CARD DESIGN

I need an eye catching , simple business card design that will match my logo . I need 2 versions of it ( white background and black background) - SOME PEOPLE DID NOT GET IT AND SENDING US FRONT WHITE BACK WHITE VERSIONS WHICH IS NOT CORRECT.

ONE VERSION SHOULD BE BACK AND FRONT ALL BLACK , SECOND VERSION SHOULD BE BACK AND FRONT ALL WHITE

logo psd files are attached for both versions. The business card is going to have : First Name- Last name - position - phone numbers

```html
<!DOCTYPE html>
<html lang="en">
<head>
<meta charset="utf-8">
<title>Brightlane Business Card – Black Version</title>
<link href="https://fonts.googleapis.com/css2?family=Work+Sans:wght@400;500;600&display=swap" rel="stylesheet">
<style>
  :root {
    --page-bg: #161616;
    --card-bg: #1f1f1f;
    --card-edge: #2a2a2a;
    --brand-grey: #4a4a4a;
    --text-light: #e6e6e6;
    --text-soft: #cfcfcf;
    --divider: #8a8a8a;
  }
  * { margin: 0; padding: 0; box-sizing: border-box; }
  html, body {
    width: 1200px; height: 900px; overflow: hidden;
    background: var(--page-bg);
    font-family: "Work Sans", Arial, sans-serif;
  }
  .canvas {
    position: relative; width: 1200px; height: 900px;
    display: flex; flex-direction: column; align-items: center; justify-content: center; gap: 44px;
  }
  .card {
    width: 630px; height: 360px;
    background: linear-gradient(135deg, var(--card-bg) 0%, #262626 60%, #1c1c1c 100%);
    border: 1px solid var(--card-edge);
    box-shadow: 0 18px 40px rgba(0,0,0,0.55);
    position: relative;
  }
  .brand {
    display: flex; align-items: center; gap: 14px;
    color: var(--brand-grey);
    font-weight: 600; font-size: 46px; letter-spacing: 1px;
  }
  .brand-dot {
    width: 22px; height: 22px; border-radius: 50%;
    background: var(--brand-grey);
  }
  .card-front { display: flex; align-items: center; justify-content: center; }
  .card-front .brand { color: #8c8c8c; }
  .card-front .brand-dot { background: #8c8c8c; }
  .card-back { display: flex; align-items: center; }
  .card-back .brand { font-size: 40px; position: absolute; left: 48px; top: 150px; }
  .divider {
    position: absolute; left: 345px; top: 80px;
    width: 1px; height: 200px; background: var(--divider);
  }
  .contact {
    position: absolute; left: 375px; top: 88px;
    color: var(--text-soft);
  }
  .contact-name {
    font-size: 22px; font-weight: 500; letter-spacing: 1.5px;
    color: var(--text-light); text-transform: uppercase;
  }
  .contact-role { font-size: 17px; margin-top: 2px; margin-bottom: 16px; }
  .contact-address { font-size: 16px; line-height: 21px; margin-bottom: 8px; }
  .contact-line {
    display: flex; align-items: center; gap: 9px;
    font-size: 17px; line-height: 25px; color: var(--text-light);
  }
  .contact-line svg { width: 13px; height: 13px; flex: none; }
</style>
</head>
<body>
<main class="canvas">
  <section class="card card-front" aria-label="Card front">
    <div class="brand"><span class="brand-dot"></span>Brightlane</div>
  </section>

  <section class="card card-back" aria-label="Card back">
    <div class="brand"><span class="brand-dot"></span>Brightlane</div>
    <div class="divider"></div>
    <div class="contact">
      <p class="contact-name">Daniel Porter</p>
      <p class="contact-role">Director</p>
      <p class="contact-address">215 Harlow Street<br>Austin, TX 78704</p>
      <p class="contact-line">
        <svg viewBox="0 0 16 16" fill="none" stroke="#cfcfcf" stroke-width="1.6"><path d="M4 1.5l2.5 3-1.5 1.5c1 2 2.5 3.5 4.5 4.5l1.5-1.5 3 2.5-1.5 2.5C7 14 2 9 1.5 3z"/></svg>
        +1 512-555-0148
      </p>
      <p class="contact-line">
        <svg viewBox="0 0 16 16" fill="none" stroke="#cfcfcf" stroke-width="1.6"><rect x="1.5" y="3" width="13" height="10"/><path d="M1.5 3l6.5 6 6.5-6"/></svg>
        hello@brightlane.com
      </p>
      <p class="contact-line">
        <svg viewBox="0 0 16 16" fill="none" stroke="#cfcfcf" stroke-width="1.4"><circle cx="8" cy="8" r="6.5"/><ellipse cx="8" cy="8" rx="3" ry="6.5"/><path d="M1.5 8h13"/></svg>
        www.brightlane.com
      </p>
    </div>
  </section>
</main>
</body>
</html>
```